Webdesign für freie Trauungen
Zielgruppe
Webseite für Hochzeitspaare, Trauerende, Bestatter, Interessierte
Aufgabenstellung
Internetseite
Briefing:
Onepager
Internetseite soll wirken:
Modern
Schlank
Klar
Vertrauenserweckend
professionell
Home:
Reden für besondere Momente im Leben
Schrift an Flyer anpassen
REDEN.
ERZÄHLEN.
ERINNERN.
BERÜHREN.
Bild von mir,
Dazu, meine Reden sind:
freundlich
authentisch
ehrlich
einfühlsam
taktvoll
humorvoll
tiefsinnig
tröstend
nett
zugewandt
interessant
nach Euren Wünschen
mit Euren Inhalten
individuell
sehr persönlich
kreativ
wortgewandt
erfahren
Sprechen Sie mich an! ?
FREIE TRAUUNG:
EINFACH HIMMLISCH!
eine Liebesgeschichte erzählen
Sich ein Versprechen geben
JA zueinander sagen
Mit lieben Menschen feiern
wo, wann, wie - das entscheidet Ihr!
Segensfeier - Willkommensfeier:
im Leben willkommen heißen
Was bedeutet der Name des Kindes?
Was wollt Ihr Eurem Kind mitgeben?
Was wünscht Ihr Euch für Euer Kind?
TRAUERFEIER:
an schöne Momente erinnern
Einen Menschen mit Worten lebendig werden lassen
Mit einer persönlichen und bewegenden Ansprache
Mit all dem, was Sie sich wünschen!
REDEN ZU GEBURTSTAGEN:
mit Humor, Witz und Verstand gemeinsam zurück schauen
Und von Träumen und Sehnsüchten erzählen
Reden zum Jubiläum:
gemeinsam zurück schauen
Geleistetes würdigen
Veränderungen verständlich machen
Ausblicke wagen
Biographien:
festhalten, damit nichts von Ihrer Lebensgeschichte verloren geht
Sie erinnern sich und ich schreibe auf
Referenzen:
???? Wie am besten ???
Persönliches Vita:
Studium an der Offenen Hochschule Berlin:
- Publizistik
Germanistik
Volkswirtschaftslehre
Lateinamerikanistik
Abschluß: Magistra Artium
Freie Rednerin seit 1998
Telefonnummer 015239870461
Email: doris.Kellmeyer@postfeld.de
Wirk..

```html
<!DOCTYPE html>
<html lang="de">
<head>
<meta charset="utf-8">
<title>Kellmeyer Reden</title>
<link href="https://fonts.googleapis.com/css2?family=Open+Sans:ital,wght@0,300;0,400;0,600;0,700;1,400;1,600;1,700&display=swap" rel="stylesheet">
<style>
:root{
  --teal:#5f9592;
  --teal-light:#cfe0de;
  --panel:#f3f5f4;
  --text:#4a4a4a;
  --muted:#7a7a7a;
  --white:#ffffff;
  --dark:#2e2e2e;
}
*{margin:0;padding:0;box-sizing:border-box}
html,body{width:1200px;height:4564px;overflow:hidden}
body{font-family:"Open Sans",sans-serif;color:var(--text);background:var(--white);position:relative}
.abs{position:absolute}
.header{top:0;left:0;width:1200px;height:85px;background:var(--white)}
.brand{left:54px;top:20px;font-size:26px;font-weight:300;color:var(--text);letter-spacing:1px}
.brand small{display:block;font-size:11px;letter-spacing:9px;margin-left:34px;margin-top:-4px}
.nav{right:54px;top:35px;display:flex;gap:33px;font-size:11px;text-transform:uppercase;color:var(--text)}
.nav .active{color:var(--teal)}
.hero-panel{top:85px;left:0;width:450px;height:500px;background:var(--panel)}
.hero-photo{top:85px;left:450px;width:750px;height:500px;background:linear-gradient(90deg,#6f6c68,#a9a7a2 40%,#5b5a58 60%,#8e8c88)}
.hero-title{left:136px;top:210px;font-size:37px;font-weight:300;line-height:44px;letter-spacing:1px}
.hero-sub{left:136px;top:418px;font-size:15px;color:var(--teal);line-height:21px;text-transform:uppercase}
.portrait-circle{left:124px;top:735px;width:390px;height:390px;border-radius:50%;background:var(--teal-light)}
.portrait-figure{left:250px;top:682px;width:150px;height:443px;border-radius:70px 70px 0 0;background:linear-gradient(#e6dcc6,#a59d95 40%,#c9c6c2)}
.h2{font-size:28px;font-weight:300;text-transform:uppercase;text-align:center}
.cloud span{position:absolute;white-space:nowrap}
.btn{background:var(--teal);color:var(--white);font-size:10px;font-weight:700;text-transform:uppercase;display:flex;align-items:center;justify-content:center}
.offer-bg{top:1201px;left:0;width:1200px;height:2382px;background:var(--panel)}
.card{left:135px;width:928px;height:311px;background:var(--white);box-shadow:0 8px 24px rgba(0,0,0,.07)}
.card .img{position:absolute;left:40px;top:37px;width:357px;height:237px}
.card .txt{position:absolute;left:462px;top:56px;width:320px}
.card h3{font-size:21px;font-weight:400;color:var(--teal);line-height:28px;text-transform:uppercase;margin-bottom:18px}
.card p{font-size:16px;line-height:21px}
.card .gap{margin-top:20px}
.quote{position:absolute;right:39px;top:-14px;width:32px;height:32px;background:var(--teal)}
.vita-h{font-size:17px;color:var(--teal);text-transform:uppercase;line-height:22px}
.vita ul{font-size:12px;color:var(--muted);line-height:18px;margin:12px 0 0 16px}
.kontakt{left:386px;top:3744px;width:222px;height:286px;background:var(--panel);padding:96px 0 0 36px;font-size:12px}
.kontakt p{margin-top:12px}
.testi{top:4143px;left:0;width:1200px;height:363px;background:linear-gradient(120deg,#dfe5e4,#f6f7f7 60%,#ffffff)}
.footer{top:4506px;left:0;width:1200px;height:58px;background:var(--dark);color:var(--white);font-size:10px}
</style>
</head>
<body>
<header class="abs header">
  <div class="abs brand">Kellmeyer<small>REDEN</small></div>
  <nav class="abs nav"><span class="active">Start</span><span>Meine Reden</span><span>Was ich anbiete</span><span>Persönliches Vita</span><span>Referenzen</span></nav>
</header>

<section>
  <div class="abs hero-panel"></div>
  <div class="abs hero-photo" role="img" aria-label="Foto der Rednerin, an eine Glasscheibe gelehnt, mit Spiegelung"></div>
  <h1 class="abs hero-title">REDEN.<br>ERZÄHLEN.<br>ERINNERN.<br>BERÜHREN.</h1>
  <p class="abs hero-sub">Reden für besondere<br>Momente im Leben</p>
</section>

<section>
  <div class="abs portrait-circle"></div>
  <div class="abs portrait-figure" role="img" aria-label="Porträtfoto der Rednerin im grauen Blazer"></div>
  <h2 class="abs h2" style="left:633px;top:698px;width:400px">Meine Reden sind</h2>
  <div class="cloud">
    <span style="left:770px;top:797px;font-size:13px;font-style:italic;font-weight:600;color:#666">taktvoll</span>
    <span style="left:847px;top:797px;font-size:13px;color:#888">interessant</span>
    <span style="left:680px;top:827px;font-size:26px;font-weight:600">authentisch</span>
    <span style="left:843px;top:830px;font-size:22px;color:#666">erfahren</span>
    <span style="left:956px;top:836px;font-size:17px;font-style:italic;color:#777">tiefsinnig</span>
    <span style="left:600px;top:890px;font-size:19px;transform:rotate(-90deg);transform-origin:0 0;top:893px;left:608px;top:893px">kreativ</span>
    <span style="left:638px;top:888px;font-size:12px;font-style:italic;transform:rotate(-90deg);transform-origin:0 0">wortgewandt</span>
    <span style="left:680px;top:881px;font-size:13px;color:#888">nett</span>
    <span style="left:745px;top:870px;font-size:21px;color:#666">einfühlsam</span>
    <span style="left:895px;top:866px;font-size:25px;font-style:italic;font-weight:700;color:#666">humorvoll</span>
    <span style="left:1040px;top:942px;font-size:16px;color:#666;transform:rotate(-90deg);transform-origin:0 0">freundlich</span>
    <span style="left:589px;top:914px;font-size:21px;font-style:italic;font-weight:700">zugewandt</span>
    <span style="left:724px;top:908px;font-size:27px">nach Euren Wünschen</span>
    <span style="left:1071px;top:978px;font-size:16px;font-style:italic;font-weight:700;transform:rotate(-90deg);transform-origin:0 0">tröstend</span>
    <span style="left:685px;top:956px;font-size:21px;font-style:italic;color:#666">sehr persönlich</span>
    <span style="left:874px;top:956px;font-size:21px;font-weight:600">mit Euren Inhalten</span>
    <span style="left:716px;top:998px;font-size:15px;font-weight:600">ehrlich</span>
    <span style="left:810px;top:998px;font-size:15px;color:#666">individuell</span>
  </div>
  <div class="abs btn" style="left:750px;top:1067px;width:166px;height:28px">Sprechen Sie mich an!</div>
</section>

<section>
  <div class="abs offer-bg"></div>
  <h2 class="abs h2" style="left:0;top:1282px;width:1200px">Was ich anbiete</h2>

  <article class="abs card" style="top:1395px"><span class="quote"></span>
    <div class="img" role="img" aria-label="Foto eines lachenden Brautpaars im Blütenregen" style="background:linear-gradient(135deg,#8a8178,#e6e2dc 50%,#6d6a66)"></div>
    <div class="txt"><h3>Freie Trauung:<br>Einfach himmlisch!</h3><p>eine Liebesgeschichte erzählen<br>Sich ein Versprechen geben<br>JA zueinander sagen<br>Mit lieben Menschen feiern</p><p class="gap">wo, wann, wie – das entscheidet Ihr!</p></div>
  </article>

  <article class="abs card" style="top:1753px"><span class="quote"></span>
    <div class="img" role="img" aria-label="Foto einer Mutter mit lachendem Baby" style="background:linear-gradient(135deg,#5b4a3c,#c9a88c 50%,#e8e4dd)"></div>
    <div class="txt"><h3>Segensfeier<br>Willkommensfeier</h3><p>im Leben willkommen heißen<br>Was bedeutet der Name des Kindes?<br>Was wollt Ihr Eurem Kind mitgeben?<br>Was wünscht Ihr Euch für Euer Kind?</p></div>
  </article>

  <article class="abs card" style="top:2111px"><span class="quote"></span>
    <div class="img" role="img" aria-label="Foto eines weißen Blumenstraußes mit brennender Kerze" style="background:linear-gradient(135deg,#2b2b2e,#8d8d92 45%,#1e1e22)"></div>
    <div class="txt"><h3>Trauerfeier</h3><p>an schöne Momente erinnern<br>Einen Menschen mit Worten<br>lebendig werden lassen<br>Mit einer persönlichen und<br>bewegenden Ansprache</p><p class="gap">Mit all dem, was Sie sich wünschen!</p></div>
  </article>

  <article class="abs card" style="top:2469px"><span class="quote"></span>
    <div class="img" role="img" aria-label="Foto einer Familie bei einer Geburtstagsfeier im Garten" style="background:linear-gradient(135deg,#6e7a55,#b9a58c 50%,#4f5a44)"></div>
    <div class="txt"><h3>Reden zu Geburtstagen</h3><p>mit Humor, Witz und Verstand<br>gemeinsam zurück schauen<br>Und von Träumen und Sehnsüchten<br>erzählen</p></div>
  </article>

  <article class="abs card" style="top:2827px"><span class="quote"></span>
    <div class="img" role="img" aria-label="Foto einer feiernden Gruppe, die anstößt" style="background:linear-gradient(135deg,#3f4a55,#9aa3aa 50%,#5a4a40)"></div>
    <div class="txt"><h3>Reden zum Jubiläum</h3><p>gemeinsam zurück schauen<br>Geleistetes würdigen<br>Veränderungen verständlich machen<br>Ausblicke wagen</p></div>
  </article>

  <article class="abs card" style="top:3185px"><span class="quote"></span>
    <div class="img" role="img" aria-label="Foto einer alten Schreibmaschine auf Holztisch" style="background:linear-gradient(135deg,#6a5441,#a88a6c 50%,#4d3b2d)"></div>
    <div class="txt"><h3>Biographien</h3><p>festhalten, damit nichts von Ihrer<br>Lebensgeschichte verloren geht<br>Sie erinnern sich und ich schreibe auf</p></div>
  </article>
</section>

<section class="vita">
  <h2 class="abs h2" style="left:136px;top:3648px;text-align:left">Persönliches Vita</h2>
  <div class="abs" style="left:136px;top:3746px;width:230px">
    <h3 class="vita-h">Studium an der Offenen<br>Hochschule Berlin</h3>
    <ul><li>Publizistik</li><li>Germanistik</li><li>Volkswirtschaftslehre</li><li>Lateinamerikanistik</li><li>Abschluß: Magistra Artium</li></ul>
    <h3 class="vita-h" style="margin-top:30px">Freie Rednerin seit 1998</h3>
    <h3 class="vita-h" style="margin-top:30px">Wirkungskreis</h3>
    <p style="font-size:12px;color:var(--muted);line-height:18px;margin-top:10px">Aachen, Viersen, Düsseldorf,<br>Krefeld, Erkelenz, Neuss, Köln</p>
  </div>
  <div class="abs kontakt">
    <h3 class="vita-h" style="font-size:16px">Kontakt</h3>
    <p style="margin-top:18px">doris.kellmeyer@postfeld.de</p>
    <p>0152-39870461</p>
    <p style="color:var(--teal);font-size:11px">kellmeyerreden.de</p>
  </div>
  <div class="abs" role="img" aria-label="Porträtfoto der Rednerin mit Brille vor grünem Sessel" style="left:636px;top:3744px;width:427px;height:286px;background:linear-gradient(90deg,#2f4a3e,#d9d3c6 45%,#2d4639)"></div>
  <div class="abs btn" style="left:897px;top:4051px;width:166px;height:32px">Sprechen Sie mich an!</div>
</section>

<section>
  <div class="abs testi"></div>
  <h2 class="abs h2" style="left:0;top:4208px;width:1200px">Das sagen Kunden über mich</h2>
  <div class="abs" role="img" aria-label="Kundenfoto" style="left:562px;top:4275px;width:76px;height:76px;border-radius:50%;background:#c9a993;border:3px solid #fff"></div>
  <p class="abs" style="left:300px;top:4374px;width:600px;text-align:center;font-size:11px;color:var(--muted);line-height:15px">Sed eiusmod tempor incidunt ut labore et dolore magna aliqua. Ut enim ad minim veniam, quis nostrud exercitation ullamco laboris nisi ut aliquid ex ea commodi consequat.</p>
  <p class="abs" style="left:0;top:4414px;width:1200px;text-align:center;font-size:11px;font-weight:600">Miriam Musterfrau</p>
  <svg class="abs" style="left:575px;top:4446px" width="50" height="14"><circle cx="10" cy="7" r="5" fill="#5f9592"/><circle cx="25" cy="7" r="5" fill="#fff" stroke="#ddd"/><circle cx="40" cy="7" r="5" fill="#fff" stroke="#ddd"/></svg>
</section>

<footer class="abs footer">
  <div class="abs" style="left:54px;top:16px;font-size:18px;font-weight:300">Kellmeyer</div>
  <div class="abs" style="left:440px;top:23px;display:flex;gap:28px;text-transform:uppercase"><span>Startseite</span><span>Kontakt</span><span>Impressum</span><span>Datenschutz</span></div>
  <div class="abs" style="right:50px;top:23px;text-transform:uppercase">Copyright @2021 Doris Kellmeyer</div>
</footer>
</body>
</html>
```